Professional Business Cards

We need a nice looking, profession and modern business card for our new company. Our logo is attatched

Target Market(s)

Young Professionals

Industry/Entity Type

Financial

Contact Information for Business Card

FRONT

Vardane Ledger Pty Ltd
Level 22, Harbour Point, 48 Wattlebrook Ave
Sydney NSW 2000
ABN : 47 318 905 226

Owen Hadley - Chief Operations Officer
P : 02 9173 5528
M: 0418 356 091
owen@vardaneledger,com

BACK

- Cryptocurrency Exchange Services
- Cryptocurrency Mining Operations
- Cryptocurrency Investment Fund Offering

Font styles to use
Sans Serif

Colors
0255a3
9d9d9d

```html
<!DOCTYPE html>
<html lang="en">
<head>
<meta charset="utf-8">
<title>Vardane Ledger – Business Card</title>
<link rel="stylesheet" href="https://fonts.googleapis.com/css2?family=Roboto:wght@400;500;700&family=Roboto+Condensed:wght@700&display=swap">
<style>
  :root {
    --brand-blue: #0255a3;
    --brand-grey: #9d9d9d;
    --text-grey: #555555;
    --card-white: #f3f3f3;
    --backdrop: #2a2a2a;
    --on-blue: #ffffff;
  }
  html, body {
    margin: 0;
    padding: 0;
    width: 1200px;
    height: 960px;
    overflow: hidden;
    background: var(--backdrop);
    font-family: "Roboto", Arial, sans-serif;
  }
  .canvas {
    position: relative;
    width: 1200px;
    height: 960px;
  }
  .card {
    position: absolute;
    width: 600px;
    height: 343px;
    box-shadow: 0 4px 10px rgba(0,0,0,0.5);
    overflow: hidden;
  }
  .card-front { left: 314px; top: 113px; background: var(--card-white); }
  .card-back  { left: 311px; top: 472px; background: var(--brand-blue); }

  /* front */
  .brand {
    position: absolute;
    display: flex;
    align-items: center;
    gap: 10px;
    font-weight: 700;
    letter-spacing: 0.5px;
    white-space: nowrap;
  }
  .brand-mark {
    width: 14px;
    height: 14px;
  }
  .brand-front { left: 42px; top: 52px; font-size: 30px; color: var(--brand-blue); }
  .brand-front .brand-mark { background: var(--brand-blue); }

  .company-details {
    position: absolute;
    left: 42px;
    top: 145px;
    font-size: 14.5px;
    line-height: 18px;
    color: var(--text-grey);
  }
  .company-name { font-weight: 500; }
  .contact-list {
    list-style: none;
    margin: 9px 0 0;
    padding: 0;
  }
  .contact-list li {
    display: flex;
    align-items: center;
    gap: 8px;
    height: 19px;
  }
  .contact-icon { width: 14px; height: 14px; fill: var(--brand-blue); flex: none; }
  .abn { margin-top: 8px; }

  .person {
    position: absolute;
    right: 42px;
    top: 203px;
    text-align: right;
  }
  .person-name {
    font-family: "Roboto Condensed", "Arial Narrow", sans-serif;
    font-weight: 700;
    font-size: 22px;
    line-height: 24px;
    color: var(--brand-blue);
    text-transform: uppercase;
  }
  .person-title {
    font-size: 15px;
    line-height: 20px;
    color: var(--text-grey);
  }
  .accent-tab {
    position: absolute;
    right: 0;
    top: 202px;
    width: 15px;
    height: 45px;
    background: var(--brand-blue);
  }

  /* back */
  .brand-back { right: 33px; top: 196px; font-size: 32px; color: var(--on-blue); }
  .brand-back .brand-mark { background: var(--on-blue); }
  .services {
    position: absolute;
    right: 33px;
    top: 263px;
    list-style: none;
    margin: 0;
    padding: 0;
    text-align: right;
    color: var(--on-blue);
    font-size: 14.5px;
    line-height: 18px;
  }
  .services li::after {
    content: "";
    display: inline-block;
    width: 7px;
    height: 7px;
    margin-left: 8px;
    background: var(--on-blue);
    transform: rotate(45deg) translateY(-2px);
  }
</style>
</head>
<body>
<main class="canvas">
  <section class="card card-front" aria-label="Business card front">
    <div class="brand brand-front"><span class="brand-mark"></span>VARDANE LEDGER</div>

    <div class="company-details">
      <div class="company-name">Vardane Ledger Pty Ltd</div>
      <div>Level 22, Harbour Point</div>
      <div>48 Wattlebrook Ave</div>
      <div>Sydney NSW 2000</div>
      <ul class="contact-list">
        <li>
          <svg class="contact-icon" viewBox="0 0 24 24" aria-hidden="true"><path d="M6.6 10.8a15.1 15.1 0 0 0 6.6 6.6l2.2-2.2a1 1 0 0 1 1-.25 11.4 11.4 0 0 0 3.6.57 1 1 0 0 1 1 1V20a1 1 0 0 1-1 1A17 17 0 0 1 3 4a1 1 0 0 1 1-1h3.5a1 1 0 0 1 1 1c0 1.25.2 2.45.57 3.57a1 1 0 0 1-.25 1z"/></svg>
          <span>02 9173 5528</span>
        </li>
        <li>
          <svg class="contact-icon" viewBox="0 0 24 24" aria-hidden="true"><path d="M7 1h10a2 2 0 0 1 2 2v18a2 2 0 0 1-2 2H7a2 2 0 0 1-2-2V3a2 2 0 0 1 2-2zm0 3v14h10V4zm5 15.2a1.2 1.2 0 1 0 0 2.4 1.2 1.2 0 0 0 0-2.4z"/></svg>
          <span>0418 356 091</span>
        </li>
        <li>
          <svg class="contact-icon" viewBox="0 0 24 24" aria-hidden="true"><path d="M2 5h20v14H2zm2 2v.4l8 5 8-5V7zm0 2.8V17h16V9.8l-8 5z"/></svg>
          <span>owen@vardaneledger.com</span>
        </li>
      </ul>
      <div class="abn">ABN : 47 318 905 226</div>
    </div>

    <div class="person">
      <div class="person-name">Owen Hadley</div>
      <div class="person-title">Chief Operations Officer</div>
    </div>
    <div class="accent-tab"></div>
  </section>

  <section class="card card-back" aria-label="Business card back">
    <div class="brand brand-back"><span class="brand-mark"></span>VARDANE LEDGER</div>
    <ul class="services">
      <li>Cryptocurrency Exchange Services</li>
      <li>Cryptocurrency Mining Operations</li>
      <li>Cryptocurrency Investment Fund Offering</li>
    </ul>
  </section>
</main>
</body>
</html>
```